Plakat-Design für Softwareentwicklung
Zielgruppe
Gemeinsam mit den Kunden entwickelt Velmoria hochkomplexe, sicherheitskritische Komponenten im Bereich der Softwareentwicklung für Automotive, Medical, Avionik-, und Defence, sowie Industriesysteme, nach branchenüblichen Vorgehensmodellen und Vorgaben (https://www.velmoria-beispiel.de/).
Wir suchen ein Design für unsere Kalenderplakate für das Jahr 2019.
Die Kalenderplakate benötigen wir für unsere internen Mitarbeiter und Geschäftskunden/-partner (B2B).
Aufgabenstellung
In den letzten Jahren haben wir das Kalenderplakat sowohl in DIN A3 und DIN B1 anfertigen lassen.
Das Kalenderplakat sollte praktisch und optisch ansprechend gestaltet sein, sodass man es sich gerne als Jahresplaner in sein Büro hängt. Welche Bilder/Fotos Sie nutzen, welches Design Sie wählen, bleibt komplett Ihnen überlassen. Wir möchten hier Ihre Kreativität nicht einschränken.
Neben dem Kalender (Tage nach Monaten sortiert, die letzten beiden Monate von 2018 und die ersten beiden von 2020 bitte ebenfalls integrieren, Wochenende und Feiertage farblich hervorheben), sollten auch unsere Kontaktdaten und unser Logo auf dem Plakat abgebildet werden.
Unser Slogan lautet 'Präzise Software-Engineering'.
Wir freuen uns auf Ihre Vorschläge!

```html
<!DOCTYPE html>
<html lang="de">
<head>
<meta charset="utf-8">
<title>Velmoria Kalender 2019</title>
<link rel="stylesheet" href="https://fonts.googleapis.com/css2?family=Oswald:wght@300;400;500;600;700&display=swap">
<style>
:root{
  --panel:#3b3839;
  --title-box:#4a4344;
  --accent:#f07a1c;
  --accent-soft:#f2a36a;
  --peach:#f0b890;
  --weekend:#e2231a;
  --weekend-soft:#f08a63;
  --ink:#1d1d1d;
  --muted:#555;
  --paper:#ffffff;
}
*{margin:0;padding:0;box-sizing:border-box}
html,body{width:871px;height:1200px;overflow:hidden;background:var(--paper)}
body{position:relative;font-family:'Oswald',sans-serif;color:var(--ink)}
.side{position:absolute;left:0;top:0;width:343px;height:1200px;background:var(--panel)}
.brand{position:absolute;left:37px;top:56px;display:flex;align-items:center;gap:10px}
.brand-mark{width:14px;height:14px;background:var(--accent)}
.brand-name{font-size:32px;font-weight:400;line-height:1;color:#fff;letter-spacing:1px}
.brand-claim{position:absolute;left:37px;top:100px;font-size:10px;font-weight:400;color:#fff;letter-spacing:1.5px;text-transform:uppercase}
.hero{position:absolute;left:0;top:137px;width:343px;height:908px;
  background:linear-gradient(160deg,#5c5a5a 0%,#2f2d2d 45%,#6a4322 70%,#2a2828 100%)}
.contact{position:absolute;left:0;top:1045px;width:343px;height:155px;color:#fff;font-size:12.5px;font-weight:400;line-height:1.2}
.contact .row{position:absolute;left:64px}
.contact .row b{font-weight:500}
.contact .sep{color:var(--accent)}
.contact svg{position:absolute;left:-32px}
.title-box{position:absolute;left:343px;top:19px;width:359px;height:119px;background:var(--title-box);
  box-shadow:7px 6px 0 var(--peach);text-align:center}
.title-year{font-size:40px;font-weight:600;color:var(--accent);line-height:1;margin-top:22px}
.title-word{font-size:40px;font-weight:600;color:#fff;letter-spacing:5px;line-height:1}
.month{position:absolute;width:140px;text-align:center}
.month h2{font-size:14px;font-weight:500;color:var(--accent);text-transform:uppercase;line-height:1;height:17px}
.wd,.days{display:grid;grid-template-columns:repeat(7,1fr)}
.wd span{font-size:7.5px;color:var(--muted);text-transform:uppercase;height:17px}
.days span{font-size:10px;font-weight:500;height:22px;line-height:12px}
.six .days span{height:18.5px}
.days span:nth-child(7n+6),.days span:nth-child(7n),.days .h{color:var(--weekend)}
.adj h2{color:var(--accent-soft)}
.adj .days span{color:#333;font-weight:400}
.adj .days span:nth-child(7n+6),.adj .days span:nth-child(7n),.adj .days .h{color:var(--weekend-soft)}
</style>
</head>
<body>
<aside class="side">
  <div class="brand">
    <div class="brand-name">Velmoria</div>
    <div class="brand-mark"></div>
  </div>
  <div class="brand-claim">Präzise Software-Engineering</div>
  <div class="hero" role="img" aria-label="Nachtaufnahme einer geschwungenen Autobahnbrücke mit orangefarbenen Lichtspuren"></div>
  <div class="contact">
    <div class="row" style="top:26px">
      <svg width="16" height="18" viewBox="0 0 16 18"><path d="M8 0a6 6 0 0 0-6 6c0 4.5 6 12 6 12s6-7.5 6-12a6 6 0 0 0-6-6zm0 8.5A2.5 2.5 0 1 1 8 3.5a2.5 2.5 0 0 1 0 5z" fill="#fff"/></svg>
      <b>HEADQUARTER</b> <span class="sep">//</span> Lindenweg 14b, 80331 Munich<br><span style="padding-left:84px">Germany</span>
    </div>
    <div class="row" style="top:63px">
      <svg width="16" height="16" viewBox="0 0 16 16" style="top:4px"><path d="M3.5 0.5l2.5 3.5-1.6 1.8c.9 2.3 2.8 4.2 5.2 5.2L11.4 9.4l3.6 2.5-1.3 3.1C6.8 15 1 9.2 .5 2z" fill="#fff"/></svg>
      <b>PHONE</b> <span class="sep">//</span> +49 89 555012 – 0<br>
      <b>FAX</b> <span class="sep">//</span> +49 89 555012-99
    </div>
    <div class="row" style="top:103px">
      <svg width="18" height="13" viewBox="0 0 18 13" style="top:2px"><rect x="0.75" y="0.75" width="16.5" height="11.5" fill="none" stroke="#fff" stroke-width="1.5"/><path d="M1 1l8 7 8-7M1 12l6-5M17 12l-6-5" fill="none" stroke="#fff" stroke-width="1.3"/></svg>
      info@velmoria-beispiel.de
    </div>
    <div class="row" style="top:128px">
      <svg width="18" height="18" viewBox="0 0 18 18"><g fill="none" stroke="#fff" stroke-width="1"><circle cx="9" cy="9" r="8"/><ellipse cx="9" cy="9" rx="3.5" ry="8"/><path d="M1 9h16M2.5 5h13M2.5 13h13"/></g></svg>
      www.velmoria-beispiel.de
    </div>
  </div>
</aside>

<header class="title-box">
  <div class="title-year">2019</div>
  <div class="title-word">KALENDER</div>
</header>

<main class="calendar">
<section class="month adj" style="left:535px;top:169px"><h2>November</h2>
<div class="wd"><span>Mo</span><span>Di</span><span>Mi</span><span>Do</span><span>Fr</span><span>Sa</span><span>So</span></div>
<div class="days"><span></span><span></span><span></span><span>1</span><span>2</span><span>3</span><span>4</span><span>5</span><span>6</span><span>7</span><span>8</span><span>9</span><span>10</span><span>11</span><span>12</span><span>13</span><span>14</span><span>15</span><span>16</span><span>17</span><span>18</span><span>19</span><span>20</span><span>21</span><span>22</span><span>23</span><span>24</span><span>25</span><span>26</span><span>27</span><span>28</span><span>29</span><span>30</span></div></section>

<section class="month adj six" style="left:698px;top:169px"><h2>Dezember</h2>
<div class="wd"><span>Mo</span><span>Di</span><span>Mi</span><span>Do</span><span>Fr</span><span>Sa</span><span>So</span></div>
<div class="days"><span></span><span></span><span></span><span></span><span></span><span>1</span><span>2</span><span>3</span><span>4</span><span>5</span><span>6</span><span>7</span><span>8</span><span>9</span><span>10</span><span>11</span><span>12</span><span>13</span><span>14</span><span>15</span><span>16</span><span>17</span><span>18</span><span>19</span><span>20</span><span>21</span><span>22</span><span>23</span><span>24</span><span class="h">25</span><span class="h">26</span><span>27</span><span>28</span><span>29</span><span>30</span><span>31</span></div></section>

<section class="month" style="left:373px;top:337px"><h2>Januar</h2>
<div class="wd"><span>Mo</span><span>Di</span><span>Mi</span><span>Do</span><span>Fr</span><span>Sa</span><span>So</span></div>
<div class="days"><span></span><span class="h">1</span><span>2</span><span>3</span><span>4</span><span>5</span><span>6</span><span>7</span><span>8</span><span>9</span><span>10</span><span>11</span><span>12</span><span>13</span><span>14</span><span>15</span><span>16</span><span>17</span><span>18</span><span>19</span><span>20</span><span>21</span><span>22</span><span>23</span><span>24</span><span>25</span><span>26</span><span>27</span><span>28</span><span>29</span><span>30</span><span>31</span></div></section>

<section class="month" style="left:535px;top:337px"><h2>Februar</h2>
<div class="wd"><span>Mo</span><span>Di</span><span>Mi</span><span>Do</span><span>Fr</span><span>Sa</span><span>So</span></div>
<div class="days"><span></span><span></span><span></span><span></span><span>1</span><span>2</span><span>3</span><span>4</span><span>5</span><span>6</span><span>7</span><span>8</span><span>9</span><span>10</span><span>11</span><span>12</span><span>13</span><span>14</span><span>15</span><span>16</span><span>17</span><span>18</span><span>19</span><span>20</span><span>21</span><span>22</span><span>23</span><span>24</span><span>25</span><span>26</span><span>27</span><span>28</span></div></section>

<section class="month" style="left:698px;top:337px"><h2>März</h2>
<div class="wd"><span>Mo</span><span>Di</span><span>Mi</span><span>Do</span><span>Fr</span><span>Sa</span><span>So</span></div>
<div class="days"><span></span><span></span><span></span><span></span><span>1</span><span>2</span><span>3</span><span>4</span><span>5</span><span>6</span><span>7</span><span>8</span><span>9</span><span>10</span><span>11</span><span>12</span><span>13</span><span>14</span><span>15</span><span>16</span><span>17</span><span>18</span><span>19</span><span>20</span><span>21</span><span>22</span><span>23</span><span>24</span><span>25</span><span>26</span><span>27</span><span>28</span><span>29</span><span>30</span><span>31</span></div></section>

<section class="month" style="left:373px;top:505px"><h2>April</h2>
<div class="wd"><span>Mo</span><span>Di</span><span>Mi</span><span>Do</span><span>Fr</span><span>Sa</span><span>So</span></div>
<div class="days"><span>1</span><span>2</span><span>3</span><span>4</span><span>5</span><span>6</span><span>7</span><span>8</span><span>9</span><span>10</span><span>11</span><span>12</span><span>13</span><span>14</span><span>15</span><span>16</span><span>17</span><span>18</span><span class="h">19</span><span>20</span><span>21</span><span class="h">22</span><span>23</span><span>24</span><span>25</span><span>26</span><span>27</span><span>28</span><span>29</span><span>30</span></div></section>

<section class="month" style="left:535px;top:507px"><h2>Mai</h2>
<div class="wd"><span>Mo</span><span>Di</span><span>Mi</span><span>Do</span><span>Fr</span><span>Sa</span><span>So</span></div>
<div class="days"><span></span><span></span><span class="h">1</span><span>2</span><span>3</span><span>4</span><span>5</span><span>6</span><span>7</span><span>8</span><span>9</span><span>10</span><span>11</span><span>12</span><span>13</span><span>14</span><span>15</span><span>16</span><span>17</span><span>18</span><span>19</span><span>20</span><span>21</span><span>22</span><span>23</span><span>24</span><span>25</span><span>26</span><span>27</span><span>28</span><span>29</span><span class="h">30</span><span>31</span></div></section>

<section class="month" style="left:698px;top:507px"><h2>Juni</h2>
<div class="wd"><span>Mo</span><span>Di</span><span>Mi</span><span>Do</span><span>Fr</span><span>Sa</span><span>So</span></div>
<div class="days"><span></span><span></span><span></span><span></span><span></span><span>1</span><span>2</span><span>3</span><span>4</span><span>5</span><span>6</span><span>7</span><span>8</span><span>9</span><span class="h">10</span><span>11</span><span>12</span><span>13</span><span>14</span><span>15</span><span>16</span><span>17</span><span>18</span><span>19</span><span>20</span><span>21</span><span>22</span><span>23</span><span>24</span><span>25</span><span>26</span><span>27</span><span>28</span><span>29</span><span>30</span></div></section>

<section class="month" style="left:373px;top:677px"><h2>Juli</h2>
<div class="wd"><span>Mo</span><span>Di</span><span>Mi</span><span>Do</span><span>Fr</span><span>Sa</span><span>So</span></div>
<div class="days"><span>1</span><span>2</span><span>3</span><span>4</span><span>5</span><span>6</span><span>7</span><span>8</span><span>9</span><span>10</span><span>11</span><span>12</span><span>13</span><span>14</span><span>15</span><span>16</span><span>17</span><span>18</span><span>19</span><span>20</span><span>21</span><span>22</span><span>23</span><span>24</span><span>25</span><span>26</span><span>27</span><span>28</span><span>29</span><span>30</span><span>31</span></div></section>

<section class="month" style="left:535px;top:677px"><h2>August</h2>
<div class="wd"><span>Mo</span><span>Di</span><span>Mi</span><span>Do</span><span>Fr</span><span>Sa</span><span>So</span></div>
<div class="days"><span></span><span></span><span></span><span>1</span><span>2</span><span>3</span><span>4</span><span>5</span><span>6</span><span>7</span><span>8</span><span>9</span><span>10</span><span>11</span><span>12</span><span>13</span><span>14</span><span>15</span><span>16</span><span>17</span><span>18</span><span>19</span><span>20</span><span>21</span><span>22</span><span>23</span><span>24</span><span>25</span><span>26</span><span>27</span><span>28</span><span>29</span><span>30</span><span>31</span></div></section>

<section class="month six" style="left:698px;top:677px"><h2>September</h2>
<div class="wd"><span>Mo</span><span>Di</span><span>Mi</span><span>Do</span><span>Fr</span><span>Sa</span><span>So</span></div>
<div class="days"><span></span><span></span><span></span><span></span><span></span><span></span><span>1</span><span>2</span><span>3</span><span>4</span><span>5</span><span>6</span><span>7</span><span>8</span><span>9</span><span>10</span><span>11</span><span>12</span><span>13</span><span>14</span><span>15</span><span>16</span><span>17</span><span>18</span><span>19</span><span>20</span><span>21</span><span>22</span><span>23</span><span>24</span><span>25</span><span>26</span><span>27</span><span>28</span><span>29</span><span>30</span></div></section>

<section class="month" style="left:373px;top:851px"><h2>Oktober</h2>
<div class="wd"><span>Mo</span><span>Di</span><span>Mi</span><span>Do</span><span>Fr</span><span>Sa</span><span>So</span></div>
<div class="days"><span></span><span>1</span><span>2</span><span class="h">3</span><span>4</span><span>5</span><span>6</span><span>7</span><span>8</span><span>9</span><span>10</span><span>11</span><span>12</span><span>13</span><span>14</span><span>15</span><span>16</span><span>17</span><span>18</span><span>19</span><span>20</span><span>21</span><span>22</span><span>23</span><span>24</span><span>25</span><span>26</span><span>27</span><span>28</span><span>29</span><span>30</span><span>31</span></div></section>

<section class="month" style="left:535px;top:851px"><h2>November</h2>
<div class="wd"><span>Mo</span><span>Di</span><span>Mi</span><span>Do</span><span>Fr</span><span>Sa</span><span>So</span></div>
<div class="days"><span></span><span></span><span></span><span></span><span>1</span><span>2</span><span>3</span><span>4</span><span>5</span><span>6</span><span>7</span><span>8</span><span>9</span><span>10</span><span>11</span><span>12</span><span>13</span><span>14</span><span>15</span><span>16</span><span>17</span><span>18</span><span>19</span><span>20</span><span>21</span><span>22</span><span>23</span><span>24</span><span>25</span><span>26</span><span>27</span><span>28</span><span>29</span><span>30</span></div></section>

<section class="month six" style="left:698px;top:851px"><h2>Dezember</h2>
<div class="wd"><span>Mo</span><span>Di</span><span>Mi</span><span>Do</span><span>Fr</span><span>Sa</span><span>So</span></div>
<div class="days"><span></span><span></span><span></span><span></span><span></span><span></span><span>1</span><span>2</span><span>3</span><span>4</span><span>5</span><span>6</span><span>7</span><span>8</span><span>9</span><span>10</span><span>11</span><span>12</span><span>13</span><span>14</span><span>15</span><span>16</span><span>17</span><span>18</span><span>19</span><span>20</span><span>21</span><span>22</span><span>23</span><span>24</span><span class="h">25</span><span class="h">26</span><span>27</span><span>28</span><span>29</span><span>30</span><span>31</span></div></section>

<section class="month adj" style="left:373px;top:1021px"><h2>Januar</h2>
<div class="wd"><span>Mo</span><span>Di</span><span>Mi</span><span>Do</span><span>Fr</span><span>Sa</span><span>So</span></div>
<div class="days"><span></span><span></span><span class="h">1</span><span>2</span><span>3</span><span>4</span><span>5</span><span>6</span><span>7</span><span>8</span><span>9</span><span>10</span><span>11</span><span>12</span><span>13</span><span>14</span><span>15</span><span>16</span><span>17</span><span>18</span><span>19</span><span>20</span><span>21</span><span>22</span><span>23</span><span>24</span><span>25</span><span>26</span><span>27</span><span>28</span><span>29</span><span>30</span><span>31</span></div></section>

<section class="month adj" style="left:535px;top:1021px"><h2>Februar</h2>
<div class="wd"><span>Mo</span><span>Di</span><span>Mi</span><span>Do</span><span>Fr</span><span>Sa</span><span>So</span></div>
<div class="days"><span></span><span></span><span></span><span></span><span></span><span>1</span><span>2</span><span>3</span><span>4</span><span>5</span><span>6</span><span>7</span><span>8</span><span>9</span><span>10</span><span>11</span><span>12</span><span>13</span><span>14</span><span>15</span><span>16</span><span>17</span><span>18</span><span>19</span><span>20</span><span>21</span><span>22</span><span>23</span><span>24</span><span>25</span><span>26</span><span>27</span><span>28</span><span>29</span></div></section>
</main>
</body>
</html>
```